Business cards for start-up accounting firm

I'm looking for a double sided business card ready for upload into Lumo print or similar print providers with no modification required by me.
I'm looking for something simple as i think cards that are too 'busy' actually detract from the message. I have some thoughts but more than happy to see what comes up. The logo i have came out of left field and i love it the moment i saw it!

My thoughts:

Side 1: Just the logo, perhaps on a dark grey or charcoal background to make the logo colours stand out?

Side 2: The call to action from me website 'Looking for a more relaxed, friendly and interactive relationship with your accountant?' with my contact information
Name: Gus Tarrow
Email: gus@ledgerowl.com.au
Website: www.ledgerowl.com.au
Phone: 1300 762 349

The call to action needs to be the first thing they see when they look at side 2. If it helps to know what we do and how we do it there is a draft website at www.ledgerowl.com.au

Like i said, happy to consider anything that comes up :)

Target Market(s)

i'm targeting small business owners who experience a lot of stress around finacial reporting and have had bad experiences with accountants in the past.

Industry/Entity Type

Accounting

Contact Information for Business Card

Contained in the Description

Font styles to use
Serif
Sans Serif
Other font styles liked:
• See logo files attached

Colors
474747

Requirements
Must have
• My logo, slogan and contact information

```html
<!DOCTYPE html>
<html lang="en">
<head>
<meta charset="utf-8">
<title>Ledger Owl – Business Cards</title>
<link rel="stylesheet" href="https://fonts.googleapis.com/css2?family=Source+Sans+3:ital,wght@0,400;0,600;0,700;1,400&display=swap">
<style>
  :root {
    --backdrop: #8d8d8d;
    --paper: #ecebef;
    --plum: #7a2a6e;
    --mustard: #e2b600;
    --ink: #1f1f1f;
    --slate: #6e5a6a;
    --body-text: #333333;
  }
  * { box-sizing: border-box; margin: 0; padding: 0; }
  html, body { width: 1105px; height: 1200px; overflow: hidden; }
  body {
    background: var(--backdrop);
    font-family: "Source Sans 3", Arial, sans-serif;
    position: relative;
  }
  .card {
    position: absolute;
    left: 182px;
    width: 746px;
    height: 426px;
    overflow: hidden;
  }
  .card--front { top: 119px; background: var(--paper); }
  .card--back  { top: 635px; background: var(--mustard); }

  .wordmark {
    position: absolute;
    font-weight: 700;
    font-size: 54px;
    line-height: 1;
    letter-spacing: 1px;
    white-space: nowrap;
  }
  .slogan {
    position: absolute;
    display: flex;
    align-items: center;
    gap: 10px;
    font-size: 14px;
    letter-spacing: 1.6px;
    white-space: nowrap;
  }
  .slogan::before, .slogan::after {
    content: "";
    width: 40px;
    height: 1px;
    background: currentColor;
  }

  .card--front .wordmark { left: 53px; top: 82px; color: var(--plum); }
  .card--front .slogan { left: 53px; top: 166px; color: var(--slate); }

  .holder-name {
    position: absolute;
    left: 53px;
    top: 228px;
    font-weight: 700;
    font-size: 30px;
    color: var(--plum);
  }
  .contact-list {
    position: absolute;
    left: 53px;
    top: 286px;
    list-style: none;
  }
  .contact-list li {
    display: flex;
    align-items: center;
    gap: 8px;
    height: 29px;
    font-size: 19px;
    color: var(--body-text);
  }
  .contact-list svg { width: 21px; height: 21px; flex: none; }

  .edge-band {
    position: absolute;
    left: 0;
    bottom: 0;
    width: 100%;
    height: 14px;
  }

  .card--back .wordmark { right: 50px; top: 212px; color: var(--ink); }
  .card--back .slogan { right: 50px; top: 279px; color: var(--ink); }
  .call-to-action {
    position: absolute;
    right: 50px;
    top: 312px;
    text-align: right;
    font-style: italic;
    font-size: 20px;
    line-height: 30px;
    color: var(--ink);
    white-space: nowrap;
  }
</style>
</head>
<body>

  <section class="card card--front" aria-label="Card front">
    <div class="wordmark">LEDGER OWL</div>
    <div class="slogan">CALM BOOKS, CLEAR GROWTH</div>

    <h1 class="holder-name">Gus Tarrow</h1>

    <ul class="contact-list">
      <li>
        <svg viewBox="0 0 20 20" aria-hidden="true">
          <circle cx="10" cy="10" r="10" fill="var(--plum)"/>
          <path d="M6.5 5h2l1 2.5-1.3 1c.6 1.3 1.6 2.3 2.8 2.8l1-1.3 2.5 1v2c0 .6-.5 1-1 1C9 14 6 11 5.5 6c0-.6.4-1 1-1z" fill="var(--mustard)"/>
        </svg>
        1300 762 349
      </li>
      <li>
        <svg viewBox="0 0 20 20" aria-hidden="true">
          <circle cx="10" cy="10" r="10" fill="var(--plum)"/>
          <rect x="5" y="6.5" width="10" height="7" fill="var(--mustard)"/>
          <path d="M5 6.5l5 4 5-4" fill="none" stroke="var(--plum)" stroke-width="1"/>
        </svg>
        gus@ledgerowl.com.au
      </li>
      <li>
        <svg viewBox="0 0 20 20" aria-hidden="true">
          <circle cx="10" cy="10" r="10" fill="var(--plum)"/>
          <circle cx="10" cy="10" r="5" fill="none" stroke="var(--mustard)" stroke-width="1.4"/>
          <path d="M5 10h10M10 5c-2.5 3-2.5 7 0 10M10 5c2.5 3 2.5 7 0 10" fill="none" stroke="var(--mustard)" stroke-width="1.1"/>
        </svg>
        www.ledgerowl.com.au
      </li>
    </ul>

    <svg class="edge-band" viewBox="0 0 746 14" preserveAspectRatio="none" aria-hidden="true">
      <polygon points="0,0 492,0 486,14 0,14" fill="var(--plum)"/>
      <polygon points="497,0 746,0 746,14 491,14" fill="var(--mustard)"/>
    </svg>
  </section>

  <section class="card card--back" aria-label="Card back">
    <div class="wordmark">LEDGER OWL</div>
    <div class="slogan">CALM BOOKS, CLEAR GROWTH</div>
    <p class="call-to-action">
      Wanting a calmer, warmer<br>
      and far more open partnership<br>
      with your tax adviser?
    </p>
  </section>

</body>
</html>
```